Home Care company needs letter head branding

Home care company needs a letter head which can be used for all documents the company's clients view. We provided in home care for the elderly. We would like to use our company colors (2785A7, 0A4057 and 34A74D) and should not be too large as we will be using it on more than just a letter head but all documents our clients sign / receive.
Target Market(s)
Professional business
Industry/Entity Type
Health Care
Requirements
Must have
- corporate brand colors

```html
<!DOCTYPE html>
<html lang="en">
<head>
<meta charset="utf-8">
<title>Maplevine Care Letterhead</title>
<link href="https://fonts.googleapis.com/css2?family=PT+Sans:wght@400&family=Open+Sans:wght@400&display=swap" rel="stylesheet">
<style>
  :root {
    --brand-blue: #2785A7;
    --brand-navy: #0A4057;
    --brand-green: #34A74D;
    --brand-lime: #8DC63F;
    --ink-muted: #6b7278;
    --watermark: #eeeeee;
    --backdrop: #a9dbe3;
    --paper: #ffffff;
  }
  html, body {
    margin: 0;
    padding: 0;
    width: 1200px;
    height: 784px;
    overflow: hidden;
    background: var(--backdrop);
  }
  .letterhead {
    position: absolute;
    left: 338px;
    top: 22px;
    width: 524px;
    height: 740px;
    background: var(--paper);
    overflow: hidden;
    box-shadow: 0 6px 18px rgba(10, 64, 87, 0.18);
  }
  .corner-marks {
    position: absolute;
    display: flex;
    align-items: flex-start;
    gap: 3px;
  }
  .corner-marks span { display: block; height: 4px; }
  .corner-marks .mark-navy { width: 22px; background: var(--brand-navy); }
  .corner-marks .mark-lime { width: 22px; background: var(--brand-lime); }
  .corner-marks--top-left { left: 0; top: 0; }
  .corner-marks--top-left .mark-navy { width: 4px; height: 14px; }
  .corner-marks--top-left .mark-lime { width: 24px; height: 4px; margin-left: 20px; }
  .corner-marks--top-right { right: 0; top: 0; }
  .corner-marks--top-right .mark-navy { height: 4px; margin-top: 12px; }
  .corner-marks--top-right .mark-lime { height: 4px; }

  .brand {
    position: absolute;
    left: 16px;
    top: 20px;
    display: flex;
    align-items: center;
    gap: 8px;
  }
  .brand-name {
    font-family: "PT Sans", sans-serif;
    font-size: 25px;
    color: var(--brand-blue);
    letter-spacing: 0.2px;
  }
  .brand-dot {
    width: 26px;
    height: 26px;
    border-radius: 50%;
    background: var(--brand-blue);
  }

  .contact {
    position: absolute;
    right: 26px;
    top: 22px;
    margin: 0;
    padding: 0;
    list-style: none;
    font-family: "Open Sans", sans-serif;
    font-size: 7px;
    line-height: 11px;
    color: var(--ink-muted);
    white-space: nowrap;
  }
  .contact li { display: flex; align-items: center; gap: 4px; }
  .contact svg { width: 7px; height: 7px; fill: var(--ink-muted); flex: none; }
  .contact .no-icon { padding-left: 11px; }

  .watermark {
    position: absolute;
    left: -70px;
    top: 170px;
    width: 430px;
    height: 420px;
    border-radius: 50%;
    background: radial-gradient(circle, var(--watermark) 0%, rgba(238,238,238,0.6) 55%, rgba(255,255,255,0) 72%);
  }

  .footer-swoosh {
    position: absolute;
    left: 0;
    bottom: 0;
    width: 524px;
    height: 150px;
  }
</style>
</head>
<body>
  <main class="letterhead">
    <div class="corner-marks corner-marks--top-left"><span class="mark-navy"></span><span class="mark-lime"></span></div>
    <div class="corner-marks corner-marks--top-right"><span class="mark-navy"></span><span class="mark-lime"></span></div>

    <header class="brand">
      <span class="brand-name">Maplevine Care</span>
      <span class="brand-dot"></span>
    </header>

    <ul class="contact">
      <li><svg viewBox="0 0 10 10"><path d="M5 0a3.5 3.5 0 0 0-3.5 3.5C1.5 6 5 10 5 10s3.5-4 3.5-6.5A3.5 3.5 0 0 0 5 0zm0 5a1.5 1.5 0 1 1 0-3 1.5 1.5 0 0 1 0 3z"/></svg>1200 Sample Parkway Suite 210</li>
      <li class="no-icon">Fairview, California 94538</li>
      <li><svg viewBox="0 0 10 10"><path d="M2 0l2 2.5-1 1.2a6 6 0 0 0 2.8 2.8l1.2-1L10 8l-1.5 2C4 10 0 6 0 1.5z"/></svg>510-555-0142</li>
      <li><svg viewBox="0 0 10 10"><rect x="0" y="2" width="10" height="6"/></svg>510-555-0188</li>
      <li><svg viewBox="0 0 10 10"><rect x="0" y="2" width="10" height="6"/></svg>info@maplevinecare.com</li>
      <li><svg viewBox="0 0 10 10"><circle cx="5" cy="5" r="4.5"/></svg>www.maplevinecare.com</li>
    </ul>

    <div class="watermark" role="img" aria-label="Faint large brand decoration area"></div>

    <svg class="footer-swoosh" viewBox="0 0 524 150" preserveAspectRatio="none" aria-hidden="true">
      <defs>
        <linearGradient id="swoosh-navy" x1="0" y1="1" x2="1" y2="0">
          <stop offset="0" stop-color="#0A4057"/>
          <stop offset="1" stop-color="#2785A7"/>
        </linearGradient>
        <linearGradient id="swoosh-green" x1="0" y1="0" x2="1" y2="0">
          <stop offset="0" stop-color="#34A74D"/>
          <stop offset="1" stop-color="#8DC63F"/>
        </linearGradient>
      </defs>
      <path d="M0 150 L524 150 L524 30 Q300 110 0 140 Z" fill="url(#swoosh-navy)"/>
      <path d="M0 140 Q300 110 524 30 L524 0 Q330 95 0 128 Z" fill="url(#swoosh-green)"/>
      <rect x="0" y="146" width="524" height="4" fill="#34A74D"/>
    </svg>
  </main>
</body>
</html>
```